Business Card Design Project 4 Construction Business

I am after a creative, but sleek and simple/ clean business card design. This design will form the basis of future items and might include a logo or simply a creative way to lay out the text of my company name 'kestrel ventures'
I like the simplicity of black and white however I would also be happy to see a splash of colour introduced somehow to give the text some interest and make it stand out.
I would like a double sided card.
I am young (ish!) and professional, offering construction and project management services, what I don't want is the traditional builders type card featuring a cheesy hammer/ saw image etc.
As the company name, kestrel ventures, suggests, we focus on working closely and collaboratively together, in synergy with all stakeholders involved in the projects that we undertake
Construction

```html
<!DOCTYPE html>
<html lang="en">
<head>
<meta charset="utf-8">
<title>Kestrel Ventures – Business Cards</title>
<link rel="stylesheet" href="https://fonts.googleapis.com/css2?family=Saira:wght@300;400&display=swap">
<style>
  :root {
    --page: #ffffff;
    --card-light: #ffffff;
    --card-border: #8a8a8a;
    --ink: #111111;
    --ink-soft: #3a3a3a;
    --dark-core: #2b2b2b;
    --dark-edge: #000000;
    --accent: #5b67ea;
    --text-on-dark: #b9b9b9;
    --brand-grey: #c4c4c4;
  }
  * { box-sizing: border-box; margin: 0; padding: 0; }
  html, body {
    width: 1200px; height: 608px; overflow: hidden;
    background: var(--page);
    font-family: "Saira", "Helvetica Neue", Arial, sans-serif;
  }
  .sheet { position: relative; width: 1200px; height: 608px; }
  .card {
    position: absolute; top: 0; width: 393px; height: 607px;
  }
  .card--light { left: 0; background: var(--card-light); border: 1px solid var(--card-border); }
  .card--dark {
    background: radial-gradient(ellipse 60% 55% at 50% 48%, var(--dark-core) 0%, #141414 60%, var(--dark-edge) 100%);
  }
  .card--front-dark { left: 404px; }
  .card--back { left: 806px; width: 394px; }

  .contact {
    position: absolute; right: 62px; top: 128px; text-align: right;
  }
  .contact__name { font-size: 26px; font-weight: 400; line-height: 1; letter-spacing: 0.2px; }
  .contact__role { font-size: 20px; font-weight: 400; line-height: 1; margin-top: 6px; }
  .contact__address { margin-top: 22px; font-size: 16.5px; font-weight: 300; line-height: 26px; }
  .contact__lines { margin-top: 18px; font-size: 16.5px; font-weight: 300; line-height: 26px; }

  .card--light .contact__name,
  .card--light .contact__role { color: var(--ink); }
  .card--light .contact__address,
  .card--light .contact__lines { color: var(--ink-soft); }

  .card--dark .contact__name,
  .card--dark .contact__role { color: var(--accent); }
  .card--dark .contact__address,
  .card--dark .contact__lines { color: var(--text-on-dark); }

  .brand-mark {
    position: absolute; left: 0; right: 0; top: 460px;
    display: flex; align-items: center; justify-content: center; gap: 10px;
    font-size: 20px; font-weight: 300; letter-spacing: 2px; text-transform: uppercase;
  }
  .brand-mark__dot { width: 14px; height: 14px; border-radius: 50%; }
  .card--light .brand-mark { color: var(--ink); }
  .card--light .brand-mark__dot { background: var(--ink); }
  .card--dark .brand-mark { color: var(--accent); }
  .card--dark .brand-mark__dot { background: var(--accent); }

  .brand {
    position: absolute; left: 0; right: 0; text-align: center; color: var(--brand-grey);
    font-weight: 300; text-transform: uppercase;
  }
  .brand__primary { top: 120px; font-size: 54px; line-height: 1; letter-spacing: 1px; }
  .brand__secondary { top: 188px; font-size: 28px; line-height: 1; letter-spacing: 1px; }
  .tagline {
    position: absolute; left: 0; right: 0; top: 256px; text-align: center;
    color: #dcdcdc; font-size: 17px; font-weight: 300;
  }
  .back-dot {
    position: absolute; left: 189px; top: 436px; width: 16px; height: 16px;
    border-radius: 50%; background: var(--accent);
  }
</style>
</head>
<body>
<main class="sheet">
  <section class="card card--light" aria-label="Front of card, light version">
    <div class="contact">
      <p class="contact__name">Liam Hartley</p>
      <p class="contact__role">Director</p>
      <p class="contact__address">18 Corella St<br>Ashgrove<br>NSW 2071</p>
      <p class="contact__lines">0412 555 019<br>liam@kestrelventuresgroup.com.au<br>www.kestrelventuresgroup.com.au</p>
    </div>
    <div class="brand-mark"><span class="brand-mark__dot"></span>Kestrel Ventures</div>
  </section>

  <section class="card card--dark card--front-dark" aria-label="Front of card, dark version">
    <div class="contact">
      <p class="contact__name">Liam Hartley</p>
      <p class="contact__role">Director</p>
      <p class="contact__address">18 Corella St<br>Ashgrove<br>NSW 2071</p>
      <p class="contact__lines">0412 555 019<br>liam@kestrelventuresgroup.com.au<br>www.kestrelventuresgroup.com.au</p>
    </div>
    <div class="brand-mark"><span class="brand-mark__dot"></span>Kestrel Ventures</div>
  </section>

  <section class="card card--dark card--back" aria-label="Back of card">
    <p class="brand brand__primary">Kestrel</p>
    <p class="brand brand__secondary">Ventures</p>
    <p class="tagline">Construction &amp; Project Management</p>
    <span class="back-dot"></span>
  </section>
</main>
</body>
</html>
```